HVAC Contractor Website Design

We are working with an HVAC contractor in Idaho called QR HVAC.
Some sites to use for content/competitors and inspiration:
https://www.brindlevent.example
https://plumcrest.example/web/contractor/ (lots of contractor website designs we've approved and continue to show clients)
Thank you for taking the time to consider designing a website for us. We are web developers based in Stockton, CA, USA. Most of our projects go through the same process. Understanding this process may help you win a project with us. We custom-code all of our websites in-house. We don’t have any requirements as to what tools you use for your design, but we prefer Figma files. For any design that we label as four-stars, we send it to the client for review. The client picks the final design they want us to use. Once we complete this process, we will continue to show additional clients all the four-star sites and purchase them later. Your designs will have multiple chances to sell. For better chances of success, we ask that you follow these guidelines.
IMAGES:
If you use any images or icons in the design, we ask that you have a link to the asset so we can purchase the image/icon. Most of the designs we submit do not have the customer’s images on them unless they have some great images. Be creative; show us the feeling you are trying to portray with your image choices. Use any royalty-free site you choose. We subscribe to Velmora and mainly use their images, but we can purchase images outside of Velmora.
PLEASE NOTE: we will not submit designs to clients with watermarks on the images.
FONTS:
We ask that you identify the fonts used in the design. This can be done in a message if you want. We typically use Google Fonts and Velmora Fonts.
CONTENT:
We're always open to different content and ideas. We often submit designs with stock images so the client can see our vision. We typically take pictures after the website launch to use their images with our vision. Lorem Ipsum is fine for paragraphs, but we ask that you write the headers in correct English. We want to be able to show the vision and identify the sections of the website.
INSPIRATION:
We typically add a couple of links in the brief of websites we like to help you get started in your design.
REVISIONS:
We do not often ask for revisions of the designs unless we see something in the design that may not appeal to the client. If there are slight changes that we want to make, we do that in the development process.
FEEDBACK:
We rarely give feedback on designs during the design process. We are working on many website projects and do not have the time to provide feedback. We usually respond if your request is well thought out and asks specific questions, but a note asking “feedback, please” usually goes unanswered
Number of Pages Required
1 page
Look and feel
Each slider illustrates characteristics of the customer's brand and the style your logo design should communicate.

```html
<!DOCTYPE html>
<html lang="en">
<head>
<meta charset="utf-8">
<title>QR HVAC — Heating &amp; Air Conditioning Services</title>
<link rel="stylesheet" href="https://fonts.googleapis.com/css2?family=Poppins:ital,wght@0,400;0,500;0,600;0,700;1,400&display=swap">
<style>
:root{
  --blue:#1565d8;
  --blue-light:#29abe2;
  --navy:#1c2f6b;
  --orange:#ff6a13;
  --red:#f0341b;
  --ink:#1f1f1f;
  --grey:#6b6b6b;
  --line:#e3e3e3;
  --white:#ffffff;
  --dark:#1b1b1b;
}
*{box-sizing:border-box;margin:0;padding:0}
html,body{width:1200px;height:4621px;overflow:hidden}
body{font-family:'Poppins',sans-serif;color:var(--ink);background:var(--white);position:relative}
.abs{position:absolute}
.btn{position:absolute;display:flex;align-items:center;justify-content:center;color:var(--white);font-weight:500;font-size:19px;letter-spacing:.3px;text-transform:uppercase}
.btn-blue{background:linear-gradient(90deg,var(--blue-light),var(--blue))}
.btn-red{background:linear-gradient(90deg,var(--red),var(--orange))}
.photo{position:absolute}

/* header */
.topbar{left:305px;top:0;width:895px;height:36px;background:linear-gradient(90deg,var(--blue-light),var(--blue));color:var(--white);font-size:14px;display:flex;align-items:center;padding-left:36px;gap:52px}
.topbar .social{position:absolute;right:72px;top:9px;display:flex;gap:12px}
.topbar .social span{width:18px;height:18px;border-radius:50%;border:2px solid var(--white)}
.logo{display:flex;align-items:center;gap:10px;font-weight:700;color:var(--blue);white-space:nowrap}
.logo .mark{background:var(--orange)}
.header-logo{left:62px;top:40px;font-size:40px;line-height:1}
.header-logo .mark{width:22px;height:22px}
.nav{left:344px;top:60px;font-size:16px;font-weight:500;color:var(--ink)}
.nav a{position:absolute;white-space:nowrap;text-decoration:none;color:inherit}
.header-cta{left:994px;top:52px;width:145px;height:38px;font-size:15px}

/* hero */
.hero{left:0;top:104px;width:1200px;height:621px;background:linear-gradient(90deg,#f2f3f5 0%,#e7e9ec 100%)}
.hero-photo{left:560px;top:104px;width:640px;height:621px;background:linear-gradient(160deg,#d9dde2,#8fa6c8 55%,#3b5fa8)}
.eyebrow{left:72px;top:244px;font-size:19px;color:var(--red);font-weight:500}
.hero-title{left:72px;top:284px;font-size:55px;line-height:66px;font-weight:700;color:var(--dark)}
.hero-text{left:77px;top:486px;font-size:17px;line-height:21px;color:#333}
.hero-cta{left:77px;top:554px;width:194px;height:49px}
.unit{left:457px;top:657px;width:264px;height:105px;border-radius:10px;background:linear-gradient(180deg,#ffffff,#dfe2e6);box-shadow:0 6px 16px rgba(0,0,0,.15);z-index:3}

/* promos */
.promo{top:725px;height:366px}
.promo-cool{left:0;width:601px;background:linear-gradient(100deg,var(--blue-light),var(--blue) 75%,#1f4ea8)}
.promo-heat{left:601px;width:599px;background:linear-gradient(100deg,var(--red),var(--orange))}
.promo h2{position:absolute;font-size:29px;line-height:37px;font-weight:700;color:var(--white);text-transform:uppercase}
.promo-cool h2{left:75px;top:142px}
.promo-heat h2{right:68px;top:142px;text-align:right}
.promo-cool .btn{left:77px;top:274px;width:194px;height:49px}
.promo-heat .btn{right:68px;top:274px;width:194px;height:49px}
.promo svg{position:absolute}

/* about */
.about-img1{left:97px;top:1231px;width:366px;height:419px;background:linear-gradient(160deg,#c9ccd1,#6f7f95 60%,#3c4a5e)}
.about-img2{left:344px;top:1453px;width:226px;height:282px;background:linear-gradient(160deg,#9aa0a8,#cfc3ae 60%,#7c7468);border:3px solid var(--white)}
.about-title{left:653px;top:1314px;font-size:28px;font-weight:600;color:var(--navy)}
.about-text{left:657px;top:1374px;width:470px;font-size:15px;line-height:19.5px;color:var(--grey)}
.about-text p+p{margin-top:11px}
.about-cta{left:657px;top:1577px;width:190px;height:47px}

/* services */
.services{left:0;top:1821px;width:1200px;height:660px;background:linear-gradient(120deg,var(--blue-light),var(--blue) 60%,#2a5fc0)}
.section-title{position:absolute;left:0;width:1200px;text-align:center;font-size:28px;font-weight:600}
.services .section-title{top:80px;color:var(--white)}
.card{position:absolute;top:192px;width:222px;height:316px;background:var(--white)}
.card .pic{height:162px}
.card h3{margin:18px 0 0 20px;font-size:17px;font-weight:600}
.card p{margin:8px 20px 0 20px;font-size:10px;line-height:12px;color:#8a8a8a}
.card .more{display:block;margin:14px 0 0 20px;font-size:9px;font-weight:600;color:var(--red)}
.services .btn{left:504px;top:567px;width:190px;height:47px}

/* partners */
.partners-title{top:2568px;color:var(--dark)}
.partner-grid{left:260px;top:2662px;width:682px;height:199px;display:grid;grid-template-columns:repeat(4,1fr);grid-template-rows:repeat(2,1fr);border:1px solid var(--line)}
.partner-grid div{border:1px solid var(--line);display:flex;align-items:center;justify-content:center}
.partner-grid span{width:90px;height:26px;border-radius:13px;background:#d6d9de}

/* reviews */
.reviews{left:0;top:2951px;width:1200px;height:556px;background:linear-gradient(120deg,var(--blue),#2f6ed1 50%,var(--blue))}
.reviews .section-title{top:58px;color:var(--white);font-size:25px}
.review{position:absolute;top:153px;width:424px;height:281px;background:var(--white);border-radius:8px;padding:38px 38px 0 40px}
.review q{display:block;font-style:italic;font-size:17px;line-height:28px;color:var(--dark);quotes:none}
.stars{color:var(--red);font-size:20px;letter-spacing:5px;margin-top:2px}
.reviewer{display:flex;align-items:center;gap:16px;margin-top:10px}
.avatar{width:90px;height:90px;border-radius:50%;background:linear-gradient(160deg,#e8b98b,#8a5a3c);border:4px solid #f3a96a}
.reviewer b{display:block;font-size:19px;font-weight:600}
.reviewer small{color:var(--orange);font-size:15px}
.dots{left:566px;top:3443px;display:flex;gap:14px}
.dots span{width:22px;height:22px;border-radius:50%;background:var(--white)}
.dots span.off{background:transparent;border:2px solid var(--white)}

/* contact */
.contact-item{position:absolute;left:63px;display:flex;align-items:center;z-index:2}
.contact-icon{width:76px;height:76px;border-radius:50%;background:linear-gradient(160deg,var(--orange),var(--red));display:flex;align-items:center;justify-content:center;margin-right:22px;box-shadow:0 0 0 8px #fde3d6}
.contact-info{border-left:2px solid var(--red);padding-left:18px}
.contact-info small{display:block;color:var(--red);font-size:19px;text-transform:uppercase}
.contact-info strong{font-size:30px;font-weight:400;color:var(--dark);white-space:nowrap}
.worker{left:538px;top:3615px;width:287px;height:574px;background:linear-gradient(180deg,#3f66c7,#1f43a0 60%,#26337a)}
.quote-panel{left:823px;top:3674px;width:377px;height:515px;background:var(--navy)}
.quote-panel h2{position:absolute;left:52px;top:44px;color:var(--white);font-size:24px;font-weight:600}
.field{position:absolute;left:45px;width:268px;height:46px;background:var(--white);border:1px solid #c9c9c9;font-size:11px;color:#777;padding:14px 0 0 18px}
.field.msg{height:82px}
.quote-panel .btn{left:45px;top:425px;width:183px;height:45px}

/* footer */
.footer{left:0;top:4189px;width:1200px;height:382px;background:linear-gradient(120deg,#3aa6e6,var(--blue) 70%)}
.footer-logo{left:48px;top:166px;font-size:50px;line-height:1;color:var(--white)}
.footer-logo .mark{width:26px;height:26px}
.footer-heading{position:absolute;top:121px;font-size:22px;font-weight:500;color:var(--white);white-space:nowrap}
.footer-link{position:absolute;font-size:17px;color:#e6efff;white-space:nowrap}
.vline{position:absolute;width:2px;background:rgba(255,255,255,.7)}
.news-input{left:960px;top:179px;width:179px;height:36px;background:var(--white);font-size:16px;color:#777;padding:6px 0 0 12px}
.news-btn{left:960px;top:230px;width:179px;height:36px;font-size:17px}
.bottom-bar{left:0;top:4571px;width:1200px;height:50px;background:var(--dark);color:var(--white);font-size:12px;display:flex;align-items:center;justify-content:center}
</style>
</head>
<body>

<!-- Header -->
<div class="abs topbar">
  <span>✉&nbsp; hello@qrhvac.example</span>
  <span>☏&nbsp; (208) 555 0142</span>
  <div class="social"><span></span><span></span><span></span></div>
</div>
<div class="abs logo header-logo"><span class="mark"></span>QR HVAC</div>
<nav class="abs nav">
  <a style="left:0">HOME</a>
  <a style="left:90px">ABOUT</a>
  <a style="left:191px">SERVICES</a>
  <a style="left:318px">REVIEWS</a>
  <a style="left:442px">CONTACT US</a>
</nav>
<div class="btn btn-blue header-cta">Get a Quote</div>

<!-- Hero -->
<section class="abs hero"></section>
<div class="photo hero-photo" role="img" aria-label="Technician in blue cap repairing a wall-mounted air conditioner"></div>
<div class="abs eyebrow">BEST HVAC SERVICE PROVIDER</div>
<h1 class="abs hero-title">HEATING &amp; AIR<br>CONDITIONING<br>SERVICES</h1>
<p class="abs hero-text">Lorem ipsum dolor sit amet, consectetuer adipiscing elit.<br>Aenean commodo ligula eget dolor.</p>
<div class="btn btn-blue hero-cta">Get a Quote</div>
<div class="photo unit" role="img" aria-label="Indoor air conditioning unit"></div>

<!-- Promo panels -->
<section class="abs promo promo-cool">
  <svg style="left:72px;top:55px" width="72" height="72" viewBox="0 0 72 72" fill="none" stroke="#fff" stroke-width="5" stroke-linecap="round">
    <path d="M36 4v64M8 20l56 32M8 52l56-32"/>
    <path d="M28 10l8 8 8-8M28 62l8-8 8 8M10 30l11 3-3 11M62 42l-11-3 3-11M10 42l11-3-3-11M62 30l-11 3 3 11"/>
  </svg>
  <h2>Get the best air<br>conditioning<br>services</h2>
  <div class="btn btn-red">Get a Quote</div>
</section>
<section class="abs promo promo-heat">
  <svg style="right:84px;top:44px" width="72" height="72" viewBox="0 0 72 72" fill="none" stroke="#fff" stroke-width="4" stroke-linecap="round">
    <path d="M16 6c-6 6 6 10 0 18s6 10 0 16M32 6c-6 6 6 10 0 18s6 10 0 16M48 6c-6 6 6 10 0 18s6 10 0 16"/>
    <path d="M4 50h64M4 58h64M4 66h64"/>
  </svg>
  <h2>Book a professional<br>heatingservices in<br>Idaho</h2>
  <div class="btn btn-blue">Get a Quote</div>
</section>

<!-- About -->
<div class="photo about-img1" role="img" aria-label="Two technicians in hard hats installing a ceiling air duct"></div>
<div class="photo about-img2" role="img" aria-label="Technician checking a wall-mounted unit"></div>
<h2 class="abs about-title">ABOUT US</h2>
<div class="abs about-text">
  <p>Lorem ipsum dolor sit amet, consectetuer adipiscing elit. Aenean commodo ligula eget dolor. Aenean massa. Cum sociis natoque penatibus et magnis dis parturient montes, nascetur ridiculus mus.</p>
  <p>Lorem ipsum dolor sit amet, consectetuer adipiscing elit. Aenean commodo ligula eget dolor. Aenean massa. Cum sociis natoque penatibus et magnis dis parturient montes, nascetur ridiculus mus.</p>
</div>
<div class="btn btn-red about-cta">Read More</div>

<!-- Services -->
<section class="abs services">
  <h2 class="section-title">SERVICES WE PROVIDE</h2>
  <article class="card" style="left:79px">
    <div class="pic" role="img" aria-label="Technician installing an outdoor condenser unit" style="background:linear-gradient(160deg,#c7cbd0,#5d6470)"></div>
    <h3>New Installs</h3>
    <p>Lorem ipsum dolor sit amet, consectetur adipiscing elit. Ut elit tellus, luctus.</p>
    <span class="more">READ MORE</span>
  </article>
  <article class="card" style="left:352px">
    <div class="pic" role="img" aria-label="Technician servicing an indoor unit" style="background:linear-gradient(160deg,#e6e0d6,#9b8f7c)"></div>
    <h3>Maintenance</h3>
    <p>Lorem ipsum dolor sit amet, consectetur adipiscing elit. Ut elit tellus, luctus.</p>
    <span class="more">READ MORE</span>
  </article>
  <article class="card" style="left:626px">
    <div class="pic" role="img" aria-label="Technician fitting pipes" style="background:linear-gradient(160deg,#8090b0,#2f3f66)"></div>
    <h3>Pipe Fitting</h3>
    <p>Lorem ipsum dolor sit amet, consectetur adipiscing elit. Ut elit tellus, luctus.</p>
    <span class="more">READ MORE</span>
  </article>
  <article class="card" style="left:899px">
    <div class="pic" role="img" aria-label="Technician checking a pipe joint for leaks" style="background:linear-gradient(160deg,#d8d3cc,#6c6a72)"></div>
    <h3>Leak Detection</h3>
    <p>Lorem ipsum dolor sit amet, consectetur adipiscing elit. Ut elit tellus, luctus.</p>
    <span class="more">READ MORE</span>
  </article>
  <div class="btn btn-red">View All</div>
</section>

<!-- Partners -->
<h2 class="section-title partners-title">OUR PARTNERS</h2>
<div class="abs partner-grid">
  <div><span></span></div><div><span></span></div><div><span></span></div><div><span></span></div>
  <div><span></span></div><div><span></span></div><div><span></span></div><div><span></span></div>
</div>

<!-- Reviews -->
<section class="abs reviews">
  <h2 class="section-title">CUSTOMER REVIEWS</h2>
  <article class="review" style="left:158px">
    <q>Lorem ipsum dolor sit amet, consectetuer adipiscing elit. Aenean commodo ligula eget dolor aenean massa.</q>
    <div class="stars">★★★★★</div>
    <div class="reviewer"><div class="avatar" role="img" aria-label="Reviewer portrait"></div><div><b>Dana K. Whitfield</b><small>Manager</small></div></div>
  </article>
  <article class="review" style="left:639px">
    <q>Lorem ipsum dolor sit amet, consectetuer adipiscing elit. Aenean commodo ligula eget dolor aenean massa.</q>
    <div class="stars">★★★★★</div>
    <div class="reviewer"><div class="avatar" role="img" aria-label="Reviewer portrait"></div><div><b>Dana K. Whitfield</b><small>Manager</small></div></div>
  </article>
</section>
<div class="abs dots"><span></span><span class="off"></span><span></span></div>

<!-- Contact -->
<div class="photo worker" role="img" aria-label="Smiling technician in blue overalls pointing toward the quote form"></div>
<div class="contact-item" style="top:3742px">
  <div class="contact-icon"><svg width="36" height="36" viewBox="0 0 24 24" fill="#fff"><path d="M6.6 10.8a15.1 15.1 0 0 0 6.6 6.6l2.2-2.2a1 1 0 0 1 1-.25 11.4 11.4 0 0 0 3.6.57 1 1 0 0 1 1 1V20a1 1 0 0 1-1 1A17 17 0 0 1 3 4a1 1 0 0 1 1-1h3.5a1 1 0 0 1 1 1c0 1.25.2 2.45.57 3.57a1 1 0 0 1-.25 1z"/></svg></div>
  <div class="contact-info"><small>Phone</small><strong>(+1) 208 555 0199</strong></div>
</div>
<div class="contact-item" style="top:3869px">
  <div class="contact-icon"><svg width="36" height="36" viewBox="0 0 24 24" fill="#fff"><path d="M3 9l9-6 9 6v11H3z"/><path d="M3 9l9 6 9-6" fill="none" stroke="#f0341b" stroke-width="1.5"/></svg></div>
  <div class="contact-info"><small>Email</small><strong>help@qrhvac.example</strong></div>
</div>
<div class="contact-item" style="top:3998px">
  <div class="contact-icon"><svg width="36" height="36" viewBox="0 0 24 24" fill="#fff"><path d="M12 2a7 7 0 0 0-7 7c0 5.2 7 13 7 13s7-7.8 7-13a7 7 0 0 0-7-7zm0 9.5A2.5 2.5 0 1 1 12 6.5a2.5 2.5 0 0 1 0 5z"/></svg></div>
  <div class="contact-info"><small>Address</small><strong>Cedar Point, USA</strong></div>
</div>
<section class="abs quote-panel">
  <h2>GET A FREE QUOTE</h2>
  <div class="field" style="top:111px">Your Name</div>
  <div class="field" style="top:167px">Your Email</div>
  <div class="field" style="top:223px">Your Subject</div>
  <div class="field" style="top:278px">Your Phone Number</div>
  <div class="field msg" style="top:334px">Your Message</div>
  <div class="btn btn-red">Get a Quote</div>
</section>

<!-- Footer -->
<footer class="abs footer">
  <div class="abs logo footer-logo"><span class="mark"></span>QR HVAC</div>
  <div class="vline" style="left:360px;top:141px;height:130px"></div>
  <div class="vline" style="left:913px;top:141px;height:130px"></div>
  <h4 class="footer-heading" style="left:400px">Explore</h4>
  <span class="footer-link" style="left:400px;top:167px">Home</span>
  <span class="footer-link" style="left:535px;top:169px">Products</span>
  <span class="footer-link" style="left:400px;top:211px">About</span>
  <span class="footer-link" style="left:535px;top:211px">Testimonials</span>
  <span class="footer-link" style="left:400px;top:256px">Services</span>
  <span class="footer-link" style="left:538px;top:256px">Contact</span>
  <h4 class="footer-heading" style="left:723px">Quick Links</h4>
  <span class="footer-link" style="left:725px;top:171px">Privacy Policy</span>
  <span class="footer-link" style="left:725px;top:209px">Terms &amp; Conditions</span>
  <span class="footer-link" style="left:728px;top:247px">Cokkies Policy</span>
  <h4 class="footer-heading" style="left:960px">Newsletter</h4>
  <div class="abs news-input">Email Address</div>
  <div class="btn btn-red news-btn">Signup Now</div>
</footer>
<div class="abs bottom-bar">Privacy Policy | © Copyright QR HVAC 2024 |</div>

</body>
</html>
```